Need a flyer to leave behind when visiting clients or at shows

Glossy colorful tri-fold flyer with the same information that is on my web site www.palverdmks.com. I am open to a little modern or creative take on the typical brochure. I created the web site so I can provide any raw files needed from it. I would also like the ability to edit this flyer in the future in Adobe Photoshop Elements

```html
<!DOCTYPE html>
<html lang="en">
<head>
<meta charset="utf-8">
<title>Palverd Health Solutions – Tri-fold Brochure</title>
<link href="https://fonts.googleapis.com/css2?family=Montserrat:wght@400;500;600;700&display=swap" rel="stylesheet">
<style>
  :root {
    --purple: #5a4aa9;
    --purple-deep: #4b3c9c;
    --violet: #7a3fd0;
    --blue: #3d6fc4;
    --cyan: #10b6d6;
    --cyan-bright: #1ccbe6;
    --paper: #f0f0f3;
    --box: #dcdce3;
    --ink: #1f1f2b;
    --white: #ffffff;
    --backdrop: #e9eaec;
  }
  * { box-sizing: border-box; margin: 0; padding: 0; }
  html, body { width: 1200px; height: 1200px; overflow: hidden; background: var(--backdrop); }
  body { font-family: "Montserrat", sans-serif; }
  .stage { position: absolute; left: 0; top: 0; width: 1500px; height: 1500px; transform: scale(0.8); transform-origin: 0 0; }
  .sheet { position: absolute; left: 315px; width: 870px; height: 620px; overflow: hidden; }
  .sheet--outside { top: 90px; }
  .sheet--inside { top: 738px; background: var(--paper); }
  .sheet svg.art { position: absolute; left: 0; top: 0; width: 870px; height: 620px; }
  .txt { position: absolute; }

  /* outside */
  .tagline { left: 608px; top: 53px; color: var(--violet); font-size: 16px; line-height: 19px; font-weight: 500; }
  .ceo-name { left: 26px; top: 280px; color: var(--white); font-size: 12px; font-weight: 600; line-height: 14px; }
  .ceo-name span { font-weight: 500; font-size: 11.5px; }
  .ceo-bio { left: 28px; top: 332px; width: 230px; color: var(--white); font-size: 11px; line-height: 13.4px; }
  .contact-title { left: 325px; top: 376px; color: var(--white); font-size: 16px; font-weight: 700; }
  .contact-list { left: 325px; top: 407px; list-style: none; color: var(--white); font-size: 12px; font-weight: 500; }
  .contact-list li { display: flex; align-items: center; gap: 8px; height: 20px; }
  .contact-list svg { width: 14px; height: 14px; }
  .promise { left: 608px; top: 394px; color: var(--white); font-size: 16px; line-height: 19px; font-weight: 500; }
  .logo-slot { left: 700px; top: 556px; color: var(--white); font-size: 26px; font-weight: 500; }

  /* inside */
  .about { left: 25px; top: 356px; width: 250px; color: var(--white); }
  .about h2 { color: var(--violet); font-size: 19px; font-weight: 700; margin-bottom: 12px; }
  .about h3 { color: var(--violet); font-size: 13px; font-weight: 700; line-height: 15px; }
  .about p { font-size: 12.2px; line-height: 15px; margin-bottom: 14px; }
  .section-title { color: var(--violet); font-size: 15.5px; font-weight: 400; letter-spacing: .2px; }
  .section-title b { font-weight: 700; }
  .values { left: 335px; top: 0; width: 207px; height: 230px; background: var(--box); }
  .values .section-title { position: absolute; left: 0; width: 207px; top: 23px; text-align: center; }
  .value { position: absolute; width: 64px; text-align: center; color: var(--violet); font-size: 7px; line-height: 8px; }
  .value .tile { width: 62px; height: 48px; background: var(--purple); margin: 0 auto 6px; display: flex; align-items: center; justify-content: center; }
  .value .tile svg { width: 34px; height: 34px; }
  .value--lg { font-size: 11px; line-height: 12px; }
  .objective-title { left: 323px; top: 268px; }
  .objectives { left: 343px; top: 300px; list-style: none; }
  .objectives li { display: flex; align-items: center; gap: 9px; height: 46px; font-size: 11px; line-height: 13.5px; color: var(--ink); }
  .objectives svg { width: 36px; height: 34px; flex: none; }
  .services-title { left: 610px; top: 18px; }
  .services-intro { left: 611px; top: 41px; width: 245px; font-size: 11px; line-height: 13.4px; color: var(--ink); }
  .it-title { left: 622px; top: 157px; color: var(--violet); font-size: 15px; font-weight: 700; }
  .services-list { left: 606px; top: 189px; list-style: none; font-size: 11.2px; line-height: 14.4px; color: var(--ink); font-weight: 500; }
  .services-list li { display: flex; align-items: center; gap: 6px; }
  .services-list svg { width: 10px; height: 10px; flex: none; }
  .badge { left: 382px; top: 480px; width: 128px; height: 113px; background: var(--white); border: 3px solid #d9d9de; display: flex; align-items: center; justify-content: center; }
</style>
</head>
<body>
<div class="stage">

  <!-- Outside spread -->
  <section class="sheet sheet--outside">
    <svg class="art" viewBox="0 0 870 620" aria-hidden="false">
      <defs>
        <linearGradient id="outBg" x1="0" y1="0" x2="0.35" y2="1">
          <stop offset="0" stop-color="#5a4aa9"/>
          <stop offset="0.55" stop-color="#4f55b0"/>
          <stop offset="1" stop-color="#1aa9d3"/>
        </linearGradient>
        <linearGradient id="outWave" x1="0" y1="1" x2="1" y2="0">
          <stop offset="0" stop-color="#12c3e0"/>
          <stop offset="0.5" stop-color="#3a7ec8"/>
          <stop offset="1" stop-color="#5a4aa9"/>
        </linearGradient>
        <linearGradient id="deskPhoto" x1="0" y1="0" x2="1" y2="1">
          <stop offset="0" stop-color="#eef0f3"/>
          <stop offset="0.55" stop-color="#c9ccd3"/>
          <stop offset="1" stop-color="#6f7480"/>
        </linearGradient>
        <radialGradient id="portrait" cx="0.5" cy="0.45" r="0.6">
          <stop offset="0" stop-color="#b89a8a"/>
          <stop offset="0.6" stop-color="#6f6a6e"/>
          <stop offset="1" stop-color="#2a2a33"/>
        </radialGradient>
      </defs>
      <rect width="870" height="620" fill="url(#outBg)"/>
      <path d="M0,620 L0,470 C90,540 220,560 330,520 C460,470 560,450 700,470 C790,485 840,470 870,455 L870,620 Z" fill="url(#outWave)" opacity="0.55"/>
      <path d="M0,620 L0,560 C120,600 260,520 400,500 C520,485 560,520 600,560 L620,620 Z" fill="#12c3e0" opacity="0.55"/>
      <path d="M290,0 C300,230 520,380 740,372 C810,370 850,350 870,330 L870,0 Z" fill="var(--cyan)"/>
      <path d="M298,0 C320,210 510,335 700,322 C790,316 845,285 870,250 L870,0 Z" fill="url(#deskPhoto)" role="img" aria-label="Photo of hands typing on a laptop keyboard"/>
      <circle cx="60" cy="128" r="126" fill="var(--cyan)"/>
      <circle cx="55" cy="128" r="122" fill="url(#portrait)" role="img" aria-label="Portrait photo of the president and CEO"/>
    </svg>

    <p class="txt tagline">Increasing the Value<br>and Security of Your<br>Technology Resources</p>

    <p class="txt ceo-name">Dana Whitfield, MHA, MBA, CHCIO<br><span>President and CEO</span></p>
    <p class="txt ceo-bio">Dana is the founder and CEO of Palverd Health Solutions. She has been working in the technology industry for over 25 years with extensive experience in healthcare IT. Dana has held multiple roles including Chief Information Officer, Chief Information Security Officer, and the executive sponsor of multiple electronic health record (EHR) implementations. She has created and nurtured numerous successful IT departments and built strong relationships with leadership teams. Dana holds a Master’s in Business Administration and a Master’s in Healthcare Administration, and is certified with the College of Health Data Leaders (CHDL).</p>

    <h2 class="txt contact-title">Contact Us</h2>
    <ul class="txt contact-list">
      <li><svg viewBox="0 0 14 14"><circle cx="7" cy="7" r="7" fill="#fff"/><rect x="3.5" y="4.5" width="7" height="5" fill="none" stroke="#5a4aa9" stroke-width="1"/><path d="M3.5 4.5 L7 7.3 L10.5 4.5" fill="none" stroke="#5a4aa9" stroke-width="1"/></svg>dwhitfield@palverdmks.com</li>
      <li><svg viewBox="0 0 14 14"><circle cx="7" cy="7" r="7" fill="#fff"/><path d="M3.5 7 L7 4 L10.5 7 V10.5 H3.5 Z" fill="#5a4aa9"/></svg>www.palverdmks.com</li>
      <li><svg viewBox="0 0 14 14"><circle cx="7" cy="7" r="7" fill="#fff"/><path d="M5 3.8 L6.3 5.6 L5.6 6.4 Q6.6 8.3 7.8 8.6 L8.6 7.8 L10.3 9.1 L9.4 10.3 Q5.4 10 3.9 4.7 Z" fill="#5a4aa9"/></svg>555-014-2290</li>
    </ul>

    <p class="txt promise">Providing Information<br>Technology expertise<br>to post-acute care providers</p>
    <p class="txt logo-slot">Your Logo</p>
  </section>

  <!-- Inside spread -->
  <section class="sheet sheet--inside">
    <svg class="art" viewBox="0 0 870 620">
      <defs>
        <linearGradient id="teamPhoto" x1="0" y1="0" x2="0" y2="1">
          <stop offset="0" stop-color="#dde9f1"/>
          <stop offset="0.45" stop-color="#9fd3e6"/>
          <stop offset="0.75" stop-color="#18bcd8"/>
          <stop offset="1" stop-color="#00b5d4"/>
        </linearGradient>
        <linearGradient id="inWave" x1="0" y1="0" x2="1" y2="0">
          <stop offset="0" stop-color="#5a4aa9"/>
          <stop offset="0.5" stop-color="#4d5cb4"/>
          <stop offset="1" stop-color="#3a74c6"/>
        </linearGradient>
        <radialGradient id="techPhoto" cx="0.55" cy="0.5" r="0.6">
          <stop offset="0" stop-color="#4d86c8"/>
          <stop offset="0.6" stop-color="#2c4f8f"/>
          <stop offset="1" stop-color="#1b2f63"/>
        </radialGradient>
      </defs>
      <rect x="0" y="0" width="293" height="620" fill="#00b8d6"/>
      <rect x="0" y="0" width="293" height="360" fill="url(#teamPhoto)" role="img" aria-label="Photo of two healthcare professionals reviewing documents"/>
      <path d="M0,520 C90,560 200,545 293,560 C400,575 460,560 520,590 L870,560 L870,620 L0,620 Z" fill="url(#inWave)"/>
      <path d="M560,560 C700,545 790,450 820,330 C835,270 850,235 870,215 L870,620 L520,620 Z" fill="#4a62b8"/>
      <path d="M780,300 C810,260 840,230 870,215 L870,330 C850,340 820,330 780,300 Z" fill="#5fb4dc" opacity="0.8"/>
      <path d="M0,535 C100,575 220,560 320,570" fill="none" stroke="#5aa6e0" stroke-width="4" opacity="0.7"/>
      <circle cx="688" cy="430" r="145" fill="var(--cyan)"/>
      <circle cx="693" cy="430" r="141" fill="#ffffff"/>
      <circle cx="693" cy="430" r="136" fill="url(#techPhoto)" role="img" aria-label="Technology image of a hand touching hexagon tiles labelled IT and Data"/>
    </svg>

    <div class="txt about">
      <h2>About Us</h2>
      <h3>Our Mission</h3>
      <p>Partner with clients to increase the value and security of their technology tools.</p>
      <h3>Our Goal</h3>
      <p>Become the premiere consulting company for Information Technology in the post-acute care industries.</p>
    </div>

    <div class="txt values">
      <h2 class="section-title">OUR <b>CORE VALUES</b></h2>
      <div class="value" style="left:30px;top:55px">
        <div class="tile"><svg viewBox="0 0 34 34"><circle cx="17" cy="17" r="13" fill="none" stroke="#fff" stroke-width="1.2"/><circle cx="17" cy="14" r="3" fill="#fff"/><path d="M11 22 Q17 15 23 22 Z" fill="#fff"/></svg></div>CLIENT FOCUSED</div>
      <div class="value" style="left:110px;top:55px">
        <div class="tile"><svg viewBox="0 0 34 34"><circle cx="11" cy="10" r="3" fill="#fff"/><circle cx="23" cy="10" r="3" fill="#fff"/><rect x="7" y="15" width="20" height="3" fill="#fff"/><rect x="9" y="18" width="2" height="9" fill="#fff"/><rect x="23" y="18" width="2" height="9" fill="#fff"/><rect x="15" y="18" width="4" height="6" fill="#fff"/></svg></div>ACCOUNTABILITY</div>
      <div class="value value--lg" style="left:30px;top:137px">
        <div class="tile"><svg viewBox="0 0 34 34"><path d="M10 24 V14 Q10 6 18 6 Q26 6 26 14 L24 17 V24 Z" fill="#fff"/><path d="M14 22 H22 M18 16 V26" stroke="#5a4aa9" stroke-width="1.5"/></svg></div>INTEGRITY</div>
      <div class="value" style="left:110px;top:137px">
        <div class="tile"><svg viewBox="0 0 34 34"><circle cx="15" cy="7" r="2.5" fill="#fff"/><path d="M15 10 L13 17 L10 20 M15 10 L18 14 L21 12" stroke="#fff" stroke-width="1.8" fill="none"/><rect x="8" y="24" width="3" height="4" fill="#fff"/><rect x="13" y="22" width="3" height="6" fill="#fff"/><rect x="18" y="19" width="3" height="9" fill="#fff"/><rect x="23" y="16" width="3" height="12" fill="#fff"/></svg></div>PROFESSIONAL DEVELOPMENT</div>
    </div>

    <h2 class="txt section-title objective-title">OUR <b>PRIMARY OBJECTIVE</b></h2>
    <ul class="txt objectives">
      <li><svg viewBox="0 0 36 34" fill="none" stroke="#5a4aa9" stroke-width="2"><circle cx="18" cy="12" r="4"/><path d="M11 24 Q18 15 25 24"/><circle cx="5" cy="17" r="2.5"/><circle cx="31" cy="17" r="2.5"/><circle cx="18" cy="3" r="2"/><circle cx="18" cy="31" r="2"/></svg>Understand and exceed<br>client expectations</li>
      <li><svg viewBox="0 0 36 34" fill="none" stroke="#5a4aa9" stroke-width="2"><circle cx="9" cy="7" r="4"/><circle cx="27" cy="7" r="4"/><path d="M3 30 V18 Q9 12 15 18 V30 M21 30 V18 Q27 12 33 18 V30"/><path d="M13 22 H23"/></svg>Committed to be a partner,<br>not vendor</li>
      <li><svg viewBox="0 0 36 34" fill="none" stroke="#5a4aa9" stroke-width="2"><circle cx="18" cy="7" r="4"/><path d="M12 17 Q18 11 24 17"/><circle cx="7" cy="22" r="3.5"/><circle cx="29" cy="22" r="3.5"/><path d="M2 32 Q7 26 12 32 M24 32 Q29 26 34 32"/></svg>Provide simplified change<br>management expertise</li>
    </ul>

    <div class="txt badge">
      <svg width="100" height="90" viewBox="0 0 100 90" aria-label="Veteran status badge"><path d="M50 6 L90 22 V50 Q90 76 50 86 Q10 76 10 50 V22 Z" fill="#b9bcc6"/></svg>
    </div>

    <h2 class="txt section-title services-title">OUR <b>SERVICES</b></h2>
    <p class="txt services-intro">We understand different organizations have different needs.&nbsp; Palverd HCS strives to assist your organization by bringing solutions that are easy to understand and allow the client to track success.&nbsp; We provide solutions based on the client’s needs and desires.</p>
    <h3 class="txt it-title">Information Technology</h3>
    <ul class="txt services-list">
      <li><svg viewBox="0 0 10 10"><path d="M1 5 L4 8 L9 2" stroke="#5a4aa9" stroke-width="2" fill="none"/></svg>CIO or IT Director Services</li>
      <li><svg viewBox="0 0 10 10"><path d="M1 5 L4 8 L9 2" stroke="#5a4aa9" stroke-width="2" fill="none"/></svg>CISO or Information Security Officer</li>
      <li><svg viewBox="0 0 10 10"><path d="M1 5 L4 8 L9 2" stroke="#5a4aa9" stroke-width="2" fill="none"/></svg>Comprehensive ePHI Risk Assessments</li>
      <li><svg viewBox="0 0 10 10"><path d="M1 5 L4 8 L9 2" stroke="#5a4aa9" stroke-width="2" fill="none"/></svg>IT Department Evaluation</li>
      <li><svg viewBox="0 0 10 10"><path d="M1 5 L4 8 L9 2" stroke="#5a4aa9" stroke-width="2" fill="none"/></svg>Policy Management and Consulting</li>
      <li><svg viewBox="0 0 10 10"><path d="M1 5 L4 8 L9 2" stroke="#5a4aa9" stroke-width="2" fill="none"/></svg>On-going IT department support</li>
    </ul>
  </section>

</div>
</body>
</html>
```